TALMERA Stationary and Biz Card design
TALMERA Economic Development Company
TALMERA Stationary and Biz Card design - Financial Services
Creative Brief
Professional
Dennis P Wexford
CEO
PO BOX 782 FAIRHOLT, MAINE 04987
dennis@talmeraco.example
talmeraco.example
Looking for designs that encompass the strength and integrity of the logo.

```html
<!DOCTYPE html>
<html lang="en">
<head>
<meta charset="utf-8">
<title>TALMERA Business Card</title>
<link href="https://fonts.googleapis.com/css2?family=Open+Sans:wght@400;600;700&display=swap" rel="stylesheet">
<style>
  :root {
    --bg: #e9e7e3;
    --card: #ffffff;
    --navy: #1d3557;
    --name-blue: #2d5b8f;
    --text: #4a4a4a;
    --icon: #5c6b7a;
    --shadow: rgba(0, 0, 0, 0.18);
  }
  * { margin: 0; padding: 0; box-sizing: border-box; }
  html, body {
    width: 1200px; height: 535px; overflow: hidden;
    background: var(--bg);
    font-family: "Open Sans", Arial, sans-serif;
  }
  .canvas { position: relative; width: 1200px; height: 535px; }
  .card {
    position: absolute; top: 118px; width: 520px; height: 340px;
    background: var(--card);
    box-shadow: 0 4px 14px var(--shadow);
    overflow: hidden;
  }
  .card--front { left: 72px; }
  .card--back { left: 636px; }

  .brand {
    position: absolute; left: 36px; width: 240px;
    display: flex; flex-direction: column; align-items: center;
  }
  .card--front .brand { top: 30px; }
  .card--back .brand { top: 101px; }
  .brand__mark {
    width: 54px; height: 54px; border-radius: 50%; background: var(--navy);
    margin-bottom: 14px;
  }
  .brand__name {
    font-weight: 600; font-size: 26px; line-height: 36px;
    letter-spacing: 6px; color: var(--navy); white-space: nowrap;
  }

  .contact {
    position: absolute; left: 322px; top: 80px; list-style: none;
    font-size: 12px; color: var(--text); white-space: nowrap;
  }
  .contact li { display: flex; align-items: center; height: 21px; }
  .contact svg { width: 11px; height: 11px; margin-right: 8px; fill: var(--icon); flex: none; }

  .address {
    position: absolute; left: 20px; top: 220px;
    font-size: 12px; color: var(--text); white-space: nowrap;
  }
  .person { position: absolute; left: 322px; top: 216px; }
  .person__name { font-size: 13px; font-weight: 700; color: var(--name-blue); white-space: nowrap; }
  .person__role { font-size: 11px; color: var(--text); margin-top: 2px; }

  .website {
    position: absolute; left: 312px; top: 188px;
    font-size: 12px; color: var(--text); white-space: nowrap;
  }
</style>
</head>
<body>
<div class="canvas">
  <section class="card card--front">
    <div class="brand">
      <div class="brand__mark"></div>
      <div class="brand__name">TALMERA</div>
    </div>
    <ul class="contact">
      <li><svg viewBox="0 0 12 12"><rect x="3" y="0" width="6" height="12" rx="1.5"/></svg>310 555 0147</li>
      <li><svg viewBox="0 0 12 12"><path d="M2 1h3l1 3-2 1a7 7 0 0 0 3 3l1-2 3 1v3c-6 0-9-3-9-9z"/></svg>207 555 0182</li>
      <li><svg viewBox="0 0 12 12"><circle cx="6" cy="6" r="6"/></svg>dennis@talmeraco.example</li>
      <li><svg viewBox="0 0 12 12"><circle cx="6" cy="6" r="6"/></svg>www.talmeraco.example</li>
    </ul>
    <p class="address">Po Box 782 Fairholt, Maine 04987</p>
    <div class="person">
      <p class="person__name">Dennis P Wexford</p>
      <p class="person__role">CEO</p>
    </div>
  </section>

  <section class="card card--back">
    <div class="brand">
      <div class="brand__mark"></div>
      <div class="brand__name">TALMERA</div>
    </div>
    <p class="website">www.talmeraco.example</p>
  </section>
</div>
</body>
</html>
```